We need a flyer design to promote Penhallow & Tibbs Landscaping and Lawn Maintenance.

The flyer needs to be have:-
1) A great head line ( When quality matters)
2) A really awesome offer ( no obligation free trial mow)
3) A sense of scarcity (Due to time restraints, we can only take limited number of free lawn jobs. This offer is only available to the first 20 callers)
4) A call to action (Call now to avoid disappointment)
5) Contact details (Penhallow & Tibbs Landscaping and Lawn Maintenance 0452 786 305)

The layout of the entire flyer should come across to potential customers as

1) simple to understand what Penhallow & Tibbs offer (not overcrowd with messages; the main aim is to communicate across our services.)

The list of services that Penhallow & Tibbs provide will be:-

- Lawn Mowing - Pruning - Weeding
- Mulching - Edging - Hedging
- Trimming - Fertilising - Garden maintenance
- Weekly, fortnightly or monthly programs

Thank you.

```html
<!DOCTYPE html>
<html lang="en">
<head>
<meta charset="utf-8">
<title>Penhallow &amp; Tibbs – When Quality Matters</title>
<link rel="stylesheet" href="https://fonts.googleapis.com/css2?family=Cinzel:wght@400;500;600;700&family=Crimson+Text:wght@400;600&display=swap">
<style>
  :root {
    --page-bg: #ececec;
    --paper: #ffffff;
    --sky-top: #8fc3e6;
    --sky-mid: #cfe6f4;
    --sky-fade: #f4f9fb;
    --brown: #3a2414;
    --green-dark: #4e6e12;
    --green: #6db81f;
    --green-bright: #7ccb22;
    --green-line: #8bd43a;
    --text: #3c3c3c;
    --grass-dark: #3f7d12;
    --grass-light: #8fcf3a;
    --mower-red: #d8321c;
  }
  * { box-sizing: border-box; margin: 0; padding: 0; }
  html, body { width: 1200px; height: 1200px; overflow: hidden; }
  body { background: var(--page-bg); position: relative; }

  .flyer {
    position: absolute; left: 240px; top: 60px;
    width: 720px; height: 1080px;
    background: var(--paper);
    border: 2px solid var(--green-line);
    overflow: hidden;
    font-family: "Crimson Text", Georgia, serif;
    color: var(--text);
  }
  .sky {
    position: absolute; inset: 0 0 auto 0; height: 620px;
    background: linear-gradient(180deg, var(--sky-top) 0%, var(--sky-mid) 35%, var(--sky-fade) 70%, var(--paper) 100%);
  }
  .headline {
    position: absolute; left: 0; right: 30px; top: 110px;
    text-align: center; font-family: "Cinzel", "Times New Roman", serif;
    font-weight: 600; line-height: 0.92;
  }
  .headline span { display: block; font-size: 92px; letter-spacing: 1px; }
  .headline .when { color: var(--brown); font-weight: 700; }
  .headline .quality { color: var(--green-dark); }
  .headline .matters { color: var(--green-bright); }

  .offer-badge {
    position: absolute; left: 222px; top: 405px;
    width: 220px; height: 220px; border-radius: 50%;
    border: 3px dotted #5b5b4a;
    background: radial-gradient(circle, #ffffff 30%, #eef6e2 70%, #dcecc6 100%);
    display: flex; flex-direction: column; align-items: center; justify-content: center;
    font-family: "Cinzel", serif; text-align: center;
  }
  .offer-badge .small { font-size: 17px; color: var(--brown); letter-spacing: 1px; }
  .offer-badge .free { font-size: 72px; color: var(--green-bright); line-height: 0.95; }
  .offer-badge .trial { font-size: 26px; color: var(--brown); }

  .scarcity {
    position: absolute; left: 150px; top: 700px; width: 240px;
    font-size: 18px; line-height: 1.2; color: var(--text);
  }
  .divider-v {
    position: absolute; left: 412px; top: 640px; width: 2px; height: 140px;
    background: var(--green-line);
  }
  .services { position: absolute; left: 434px; top: 622px; width: 270px; }
  .services h2 {
    font-family: "Cinzel", serif; font-weight: 500; font-size: 28px;
    color: var(--green-dark); line-height: 1; margin-bottom: 4px;
  }
  .services ul { list-style: none; font-size: 16px; line-height: 1.2; color: var(--green-dark); }
  .services li::before { content: "• "; }

  .cta {
    position: absolute; left: 210px; top: 832px; width: 280px; text-align: center;
    font-family: "Cinzel", serif; color: var(--brown);
  }
  .cta .call { font-size: 28px; font-weight: 500; display: block; line-height: 1; }
  .cta .sub { font-size: 13px; display: block; letter-spacing: 0.5px; margin-top: 2px; }

  .grass-band { position: absolute; left: 0; top: 840px; width: 720px; height: 240px; }
  .mower {
    position: absolute; right: 0; top: 792px; width: 120px; height: 100px;
    border-radius: 40px 0 0 20px;
    background: linear-gradient(160deg, #ef5a3a, var(--mower-red) 55%, #7a1a10);
  }

  .footer-brand {
    position: absolute; left: 40px; top: 992px; width: 300px;
    font-family: "Cinzel", serif; color: var(--brown); text-align: center;
  }
  .footer-brand .name { font-size: 26px; font-weight: 700; display: block; line-height: 1; }
  .footer-brand .trade { font-size: 14px; color: var(--green); letter-spacing: 10px; display: block; margin: 3px 0 1px; }
  .footer-brand .tail { font-size: 14px; font-weight: 600; display: block; }
  .divider-foot {
    position: absolute; left: 370px; top: 975px; width: 2px; height: 80px;
    background: var(--green-line);
  }
  .contact {
    position: absolute; left: 400px; top: 968px; width: 250px; text-align: center;
    font-family: "Cinzel", serif;
  }
  .contact .label { font-size: 15px; color: var(--green-dark); letter-spacing: 4px; display: block; }
  .contact .phone { font-size: 27px; color: var(--brown); display: block; line-height: 1.1; }
</style>
</head>
<body>
  <main class="flyer">
    <div class="sky" role="img" aria-label="Blue sky with soft white clouds fading to white"></div>

    <h1 class="headline">
      <span class="when">When</span>
      <span class="quality">Quality</span>
      <span class="matters">Matters</span>
    </h1>

    <div class="offer-badge">
      <span class="small">No Obligation</span>
      <span class="free">FREE</span>
      <span class="trial">Trial Mow</span>
    </div>

    <p class="scarcity">Due to time restraints,<br>we can only take limited<br>number of free lawn jobs.<br>This offer is only available<br>to the first 20 callers</p>

    <div class="divider-v"></div>
    <section class="services">
      <h2>Services</h2>
      <ul>
        <li>Lawn Mowing</li>
        <li>Pruning • Weeding</li>
        <li>Mulching • Edging • Hedging</li>
        <li>Trimming • Fertilising</li>
        <li>Garden maintenance</li>
        <li>Weekly, fortnightly or<br>&nbsp;&nbsp;monthly programs</li>
      </ul>
    </section>

    <svg class="grass-band" viewBox="0 0 720 240" role="img" aria-label="Band of fresh green lawn grass with a curved white footer">
      <defs>
        <linearGradient id="grassFill" x1="0" y1="0" x2="0" y2="1">
          <stop offset="0" stop-color="var(--grass-light)" stop-opacity="0"/>
          <stop offset="0.3" stop-color="var(--grass-light)" stop-opacity="0.8"/>
          <stop offset="0.6" stop-color="var(--grass-dark)"/>
        </linearGradient>
      </defs>
      <rect x="0" y="0" width="720" height="240" fill="url(#grassFill)"/>
      <path d="M0 128 C200 108 360 84 480 88 C600 92 660 72 720 58 L720 240 L0 240 Z" fill="#4f8f16"/>
      <path d="M0 142 C200 122 360 98 480 102 C600 106 660 86 720 72 L720 240 L0 240 Z" fill="var(--paper)"/>
    </svg>

    <div class="mower" role="img" aria-label="Red ride-on lawn mower on the grass"></div>

    <div class="cta">
      <span class="call">Call Now</span>
      <span class="sub">To Avoid Disappointment</span>
    </div>

    <div class="footer-brand">
      <span class="name">Penhallow &amp; Tibbs</span>
      <span class="trade">Landscaping</span>
      <span class="tail">and Lawn Maintenance</span>
    </div>
    <div class="divider-foot"></div>
    <div class="contact">
      <span class="label">Maintenance</span>
      <span class="phone">0452 786 305</span>
    </div>
  </main>
</body>
</html>
```